High-End Medical Center Website Design Project

This design is part of a well thought-out project by an experienced project manager / developer. The approved wireframe is attached. Creative interpretations / suggestions based on the layout encouraged.

The design is for a new state-of-the-art medical center located in Dallas, Texas. The target audience would likely be individuals (approx. 60% female /40% male) who are the healthcare decision-makers for their families. They would likely have insurance and be inclined to seek out top-quality care.

Potential clients would choose this client over others in their industry because the medical center is physician owned, meaning it is patient-focused rather than profit-focused. The facility is brand new, featuring the latest technology. (This includes an amazing waiting room featuring WiFi and docking stations.) The physicians are hand-picked by referral only.

The look of the site should be extremely clean. We are going for a well-organized, professional look with a bit of a warm glow (interpret that however you like). Use crisp corners and the colors in the logo.

Think modern, clean with some great use of color / font.

We can get lovely photography of the medical center once construction is complete. Feel free to use an "example image" behind the Featured Area ("Physician Owned. Patient-Focused") if you like. We are open to ideas.

ONE CHANGE REQUESTED IN THE WIREFRAME:

Remove the "Connect" 1/4 page footer area and replace with a quick contact form. You may swap the "Locations" area with the form if desired. Put social media icons at the top left of the page in the top header area.

(Note: Please use social media icons that match the design rather than standard icons. We preferred not placing the icons at the top, but the client requested this. Let's not bring more attention to them than necessary.)
Updates

We're custom programming this site, so there's no need to base it on a template. Also, we would prefer not to use typical "seen everywhere" stock images.Thanks.

Industry/Entity Type

Construction

Requirements
Must have
• Follow the wireframe. This has been approved.
Nice to have
• Examples of what hover states, links or dropdowns might look like.

```html
<!DOCTYPE html>
<html lang="en">
<head>
<meta charset="utf-8">
<title>Nova Medical Center</title>
<link href="https://fonts.googleapis.com/css2?family=Montserrat:wght@400;500;700;800;900&family=Open+Sans:wght@400;600&display=swap" rel="stylesheet">
<style>
:root{
  --teal:#62b1ab;
  --teal-dark:#4f9f99;
  --navy:#3543a0;
  --navy-mid:#4352b4;
  --navy-light:#5f6fd0;
  --ink:#4a4a4a;
  --grey:#666;
  --line:#e3e3e3;
  --footer:#333;
  --white:#fff;
}
*{box-sizing:border-box;margin:0;padding:0}
html,body{width:1200px;height:1136px;overflow:hidden;background:var(--white)}
body{position:relative;font-family:"Open Sans",Arial,sans-serif;color:var(--ink)}
a{text-decoration:none;color:inherit}
.abs{position:absolute}
.display{font-family:"Montserrat",Arial,sans-serif;font-weight:800;text-transform:uppercase;letter-spacing:.04em}

/* top bar */
.topbar{top:0;left:0;width:1200px;height:46px;border-bottom:1px solid #f0f0f0}
.social{left:200px;top:13px;display:flex;gap:3px}
.social span{width:20px;height:20px;border-radius:50%;background:var(--teal);display:block}
.callnow{left:736px;top:15px;font-family:"Montserrat",sans-serif;font-size:12px;letter-spacing:.15em;color:var(--grey);text-transform:uppercase;white-space:nowrap}
.phone{right:200px;top:10px;font-family:"Montserrat",sans-serif;font-weight:700;font-size:19px;color:#555;letter-spacing:.02em;white-space:nowrap}

/* nav row */
.brand{left:200px;top:58px;width:233px;height:33px;display:flex;align-items:center;gap:7px}
.brand .mark{width:12px;height:12px;background:var(--teal);display:block;flex:none}
.brand .name{font-family:"Montserrat",sans-serif;font-weight:800;font-size:14.5px;color:var(--navy);letter-spacing:.02em;white-space:nowrap}
.nav{right:200px;top:66px;display:flex;font-family:"Montserrat",sans-serif;font-size:11.5px;letter-spacing:.08em;text-transform:uppercase;white-space:nowrap}
.nav a{color:#555;padding:0 12px;border-left:1px dotted #ccc;line-height:16px}
.nav a:first-child{border-left:none}
.nav a.active{color:var(--teal)}
.nav a:last-child{padding-right:5px}

/* hero */
.hero{top:105px;left:0;width:1200px;height:368px;background:linear-gradient(90deg,#f1e4dc 0%,#f6f4f2 22%,#fafafa 45%,#eef4f3 62%,#f5f7f7 80%,#efefef 100%)}
.hero-title{top:165px;left:0;width:1200px;text-align:center;font-size:19px}
.hero-title .a{color:var(--teal)}
.hero-title .b{color:var(--navy)}
.hero-title .dash{color:var(--navy);margin:0 8px}
.hero-text{top:199px;left:370px;width:460px;text-align:center;font-size:13.5px;line-height:17.5px;color:#666}
.circle{top:299px;width:126px;height:126px;border-radius:50%;background:var(--teal);color:var(--white);text-align:center}
.circle svg{position:absolute;left:38px;top:20px}
.circle .label{position:absolute;left:0;width:126px;top:83px;font-size:14.5px;letter-spacing:.02em}

/* band */
.band{top:473px;left:0;width:1200px;height:166px;background:linear-gradient(180deg,var(--navy) 0%,var(--navy-mid) 30%,var(--navy-light) 55%,var(--navy-mid) 80%,var(--navy) 100%)}
.apart{top:501px;right:820px;text-align:right;font-family:"Montserrat",sans-serif;font-weight:400;font-size:26px;line-height:25px;color:var(--white);text-transform:uppercase;letter-spacing:.02em}
.feature{top:501px;width:195px;color:var(--white);padding-left:12px;border-left:1px dotted rgba(255,255,255,.35);height:106px}
.feature h3{font-size:14px;margin-bottom:8px;font-family:"Montserrat",sans-serif;font-weight:800;letter-spacing:.06em;text-transform:uppercase}
.feature p{font-size:10.5px;line-height:14.6px}

/* content */
.doctor-photo{left:200px;top:671px;width:146px;height:176px;background:linear-gradient(160deg,#eef2f4 0%,#dfe7ec 45%,#c9d3dc 100%)}
.hope h2{font-size:27px;line-height:30px;letter-spacing:.02em}
.hope h2 .t{color:var(--teal)}.hope h2 .n{color:var(--navy)}
.hope{left:362px;top:670px;width:365px}
.hope p{font-size:10.3px;line-height:14.6px;color:#666;margin-top:2px}
.readmore{font-family:"Montserrat",sans-serif;font-size:15px;color:#444;text-transform:uppercase;letter-spacing:.02em;display:flex;align-items:center;gap:2px}
.hope .readmore{margin-top:8px}
.testimonials{left:743px;top:670px;width:259px;height:178px;border:1px solid #ddd;box-shadow:0 1px 3px rgba(0,0,0,.08);padding:10px 12px}
.testimonials h2{font-size:19px;color:var(--teal);padding-bottom:6px;border-bottom:2px solid #f0f0f0}
.testimonials blockquote{font-size:11.7px;line-height:15.3px;color:#555;margin-top:9px}
.testimonials .who{margin-top:6px;font-family:"Montserrat",sans-serif;font-size:12.5px;letter-spacing:.06em;color:var(--navy);text-transform:uppercase;display:flex;align-items:center;gap:5px}
.testimonials .who i{display:block;width:20px;height:1px;background:var(--navy)}
.testimonials .readmore{justify-content:flex-end;margin-top:5px}

/* footer */
.footer{top:879px;left:0;width:1200px;height:215px;background:var(--teal)}
.fcol{top:895px;color:var(--white)}
.fcol h2{font-size:19px;letter-spacing:.06em;margin-bottom:10px}
.news{left:200px;width:190px}
.news li{list-style:none;font-size:10.5px;line-height:14.6px;padding:2px 0 6px;border-bottom:1px dotted rgba(255,255,255,.35);margin-bottom:4px}
.news li:last-child{border:none}
.contact{left:403px;width:190px}
.field{background:var(--white);border:1px solid #5a9f9a;height:26px;font-size:10px;color:#999;padding:6px 8px;margin-bottom:4px}
.field.msg{height:58px}
.submit{float:right;background:linear-gradient(180deg,var(--navy-light),var(--navy));color:var(--white);font-family:"Montserrat",sans-serif;font-weight:800;font-size:12.5px;letter-spacing:.06em;padding:6px 11px;margin-top:1px}
.locations{left:608px;width:190px}
.loc{display:flex;gap:9px;margin-bottom:9px}
.loc .thumb{width:36px;height:36px;flex:none;background:linear-gradient(180deg,#8bb5d8,#d6e3ee 60%,#9aa8b3)}
.loc p{font-size:10px;line-height:13.6px}
.wait{top:879px;left:812px;width:189px;height:215px;background:var(--navy);color:var(--white);text-align:center}
.wait h2{font-size:21px;line-height:22px;margin-top:25px;letter-spacing:.03em}
.wait .num{font-family:"Montserrat",sans-serif;font-weight:900;font-size:52px;line-height:56px;margin-top:8px}
.wait .unit{font-family:"Montserrat",sans-serif;font-size:12px;letter-spacing:.08em;margin-top:-4px}
.wait p{font-size:11.7px;line-height:15.5px;margin-top:8px}

.bottom{top:1094px;left:0;width:1200px;height:42px;background:var(--footer);color:#eee;font-size:10.5px}
.bottom .copy{position:absolute;left:198px;top:13px}
.bottom .links{position:absolute;right:199px;top:13px}
.bottom .links span{margin:0 5px;color:#999}
</style>
</head>
<body>

<header>
  <div class="abs topbar"></div>
  <div class="abs social" aria-label="Social links"><span></span><span></span><span></span><span></span></div>
  <div class="abs callnow">Call Now</div>
  <div class="abs phone">(555) 014 2368</div>
  <div class="abs brand"><span class="mark"></span><span class="name">NOVA MEDICAL CENTER</span></div>
  <nav class="abs nav">
    <a class="active" href="#">Why Nova</a><a href="#">Physicians</a><a href="#">Specialities</a><a href="#">Info</a><a href="#">Locations</a><a href="#">Contact</a>
  </nav>
</header>

<section>
  <div class="abs hero" role="img" aria-label="Soft photo of a hand holding a stethoscope in front of a doctor's white coat"></div>
  <h1 class="abs hero-title display"><span class="a">Physician Owned</span><span class="dash">-</span><span class="b">Patient Focused</span></h1>
  <p class="abs hero-text">Lorem ipsum dolor sit amet, consectetuer adipiscing elit, sed diam nonummy nibh euismod tincidunt ut laoreet dolore magna aliquam erat volutpat. Ut wisi enim ad minim veniam.</p>

  <a class="abs circle" style="left:321px" href="#">
    <svg width="50" height="56" viewBox="0 0 50 56" fill="none" stroke="#fff" stroke-width="4" stroke-linecap="round"><path d="M8 4v14c0 9 6 15 12 15s12-6 12-15V4"/><path d="M20 33v8c0 7 5 11 11 11s10-5 10-12v-8"/><circle cx="41" cy="28" r="4"/></svg>
    <span class="label display">Services</span>
  </a>
  <a class="abs circle" style="left:537px" href="#">
    <svg width="50" height="56" viewBox="0 0 50 56"><path d="M4 12l34-6 2 8H4z" fill="#fff"/><rect x="4" y="14" width="42" height="30" rx="3" fill="#fff"/><circle cx="39" cy="30" r="2.5" fill="#62b1ab"/></svg>
    <span class="label display">Info</span>
  </a>
  <a class="abs circle" style="left:753px" href="#">
    <svg width="50" height="56" viewBox="0 0 50 56"><circle cx="25" cy="26" r="25" fill="#fff"/><text x="25" y="37" text-anchor="middle" font-family="Montserrat,sans-serif" font-weight="800" font-size="32" fill="#62b1ab">?</text></svg>
    <span class="label display">Help</span>
  </a>
</section>

<section>
  <div class="abs band"></div>
  <h2 class="abs apart">What Sets<br>Us Apart</h2>
  <div class="abs feature" style="left:392px"><h3>Technology</h3><p>Lorem ipsum dolor sit amet, consectetuer adipiscing elit, sed diam nonummy nibh euismod tincidunt ut laoreet dolore magna aliquam erat volutpat. Ut wisi enim.</p></div>
  <div class="abs feature" style="left:596px"><h3>Quality of Care</h3><p>Lorem ipsum dolor sit amet, consectetuer adipiscing elit, sed diam nonummy nibh euismod tincidunt ut laoreet dolore magna aliquam erat volutpat.</p></div>
  <div class="abs feature" style="left:800px"><h3>Patient Experience</h3><p>Lorem ipsum dolor sit amet, consectetuer adipiscing elit, sed diam nonummy nsed diam nonummy nibh euismod tibh euismod tincidunt ut laoreet dolore.</p></div>
</section>

<section>
  <div class="abs doctor-photo" role="img" aria-label="Photo of a senior physician in a white coat with colleagues behind"></div>
  <article class="abs hope">
    <h2 class="display"><span class="t">Heading</span> <span class="n">Hope</span></h2>
    <p>Lorem ipsum dolor sit amet, consectetuer adipiscing elit, sed diam nonummy nibh euismod tincidunt ut laoreet dolore magna aliquam erat volutpat. Ut wisi enim ad minim veniam, quis nostrud exerci tation ullamcorper suscipit lobortis nisl ut aliquip ex ea commodo consequat. Duis autem vel eum iriure dolor in hendrerit in vulputate velit esse molestie consequat, vel illum dolore eu feugiat nulla facilisis at vero eros et accumsan et iusto odio dignissim qui blandit praesent luptatum zzril delenit augue duis dolore te feugait nulla facilisi.</p>
    <a class="readmore" href="#"><svg width="14" height="10" viewBox="0 0 14 10" fill="none" stroke="#444" stroke-width="1.3"><path d="M1 1l4 4-4 4M7 1l4 4-4 4"/></svg>Read More</a>
  </article>
  <aside class="abs testimonials">
    <h2 class="display">Testimonials</h2>
    <blockquote>“Lorem ipsum dolor sit amet, consectetuer adipiscing elit, sed diam nonummy nibh euismod tincidunt ut laoreet dolore magna aliquam erat volutpat. Ut wisi enim ad minim.”</blockquote>
    <div class="who"><i></i>Dana Whitfield</div>
    <a class="readmore" href="#"><svg width="14" height="10" viewBox="0 0 14 10" fill="none" stroke="#444" stroke-width="1.3"><path d="M1 1l4 4-4 4M7 1l4 4-4 4"/></svg>Read More</a>
  </aside>
</section>

<footer>
  <div class="abs footer"></div>
  <div class="abs fcol news">
    <h2 class="display">News</h2>
    <ul>
      <li>Etiam in justo eu tortor iaculis iaculis.</li>
      <li>Morbi facilisis nunc sed nunc consequat facilisis.</li>
      <li>Phasellus imperdiet sem at neque elementum dictum.</li>
      <li>Maecenas vulputate enim porttitor elit convallis, vel tempor dolor sodales.</li>
    </ul>
  </div>
  <form class="abs fcol contact">
    <h2 class="display">Contact</h2>
    <div class="field">Name</div>
    <div class="field">Email</div>
    <div class="field msg">Message</div>
    <div class="submit">SUBMIT</div>
  </form>
  <div class="abs fcol locations">
    <h2 class="display">Locations</h2>
    <div class="loc"><div class="thumb" role="img" aria-label="Photo of clinic building"></div><p>Mauris consectetur, nunc at pharetra viverra, lacus felis accumsan sapien,</p></div>
    <div class="loc"><div class="thumb" role="img" aria-label="Photo of clinic building"></div><p>Mauris consectetur, nunc at pharetra viverra, lacus felis accumsan sapien,</p></div>
    <div class="loc"><div class="thumb" role="img" aria-label="Photo of clinic building"></div><p>Mauris consectetur, nunc at pharetra viverra, lacus felis accumsan sapien,</p></div>
  </div>
  <div class="abs wait">
    <h2 class="display">Average<br>Wait Time</h2>
    <div class="num">9</div>
    <div class="unit">MINUTES</div>
    <p>Lorem ipsum dolor sit amet,<br>consectetuer adipiscing</p>
  </div>
  <div class="abs bottom">
    <div class="copy">© 2013 Nova Medical. All rights reserved.</div>
    <div class="links">Sitemap<span>|</span>Privacy Policy</div>
  </div>
</footer>

</body>
</html>
```